Wedding Decor and Entertianment business card

Company - We run a weddings and events company called Amber Finch, we provide most entertainment and decor services to our customers.

Initial idea is ....
A simple business card with logo on the front, this will be spot varnish. On a matt black background.
The reverse will be simple contact information.

But happy to try things outside of the box and would welcome some crazy ideas.

Target Market(s)

wedding couples - 21 - 40
High end wedding venues.

Industry/Entity Type

Wedding

Contact Information for Business Card

01492 718 263
amberfinchevents.co.uk
rowan@amberfinchevents.co.uk
or
helena@amberfinchevents.co.uk

Requirements
Nice to have
• black matt background with spot varnish logo on the front.

```html
<!DOCTYPE html>
<html lang="en">
<head>
<meta charset="utf-8">
<title>Amber Finch — Business Card</title>
<link rel="stylesheet" href="https://fonts.googleapis.com/css2?family=Jost:wght@300;400&family=Quicksand:wght@400;500&display=swap">
<style>
  :root {
    --backdrop: #e4e4e6;
    --card-black: #111113;
    --card-white: #ffffff;
    --ink: #1d2230;
    --band: #16171b;
    --accent: #6a45b0;
    --text-light: #f2f2f2;
  }
  * { box-sizing: border-box; margin: 0; padding: 0; }
  html, body {
    width: 1200px; height: 1000px; overflow: hidden;
    background: var(--backdrop);
  }
  .stage {
    position: relative; width: 1200px; height: 1000px;
    display: flex; flex-direction: column; align-items: center; justify-content: center; gap: 40px;
  }
  .card {
    position: relative; width: 700px; height: 400px; border-radius: 26px; overflow: hidden;
    box-shadow: 0 10px 28px rgba(0,0,0,0.18);
  }

  /* Front */
  .card-front {
    background: repeating-linear-gradient(135deg, #141416 0 2px, #0f0f11 2px 4px);
    background-color: var(--card-black);
    display: flex; align-items: center; justify-content: center; gap: 22px;
  }
  .brand-dot {
    width: 54px; height: 54px; border: 3px solid var(--text-light); border-radius: 50%;
  }
  .brand-name {
    font-family: "Jost", sans-serif; font-weight: 300; font-size: 40px;
    letter-spacing: 0.28em; text-transform: uppercase; color: var(--text-light);
  }

  /* Back */
  .card-back { background: var(--card-white); }
  .back-brand {
    position: absolute; left: 0; top: 0; width: 330px; height: 400px;
    display: flex; flex-direction: column; align-items: center; justify-content: center; gap: 22px;
  }
  .back-brand .brand-dot { border-color: var(--ink); width: 62px; height: 62px; }
  .back-brand .brand-name { color: var(--ink); font-size: 26px; letter-spacing: 0.32em; }
  .contact-band {
    position: absolute; left: 330px; top: 0; width: 48px; height: 400px;
    background: var(--band); border-right: 3px solid var(--accent);
  }
  .contact-list {
    position: absolute; left: 330px; top: 100px; list-style: none;
  }
  .contact-item {
    display: flex; align-items: center; height: 34px;
  }
  .contact-icon {
    width: 48px; display: flex; justify-content: center;
  }
  .contact-icon svg { width: 20px; height: 20px; }
  .contact-text {
    padding-left: 16px;
    font-family: "Quicksand", sans-serif; font-weight: 500; font-size: 19px; color: var(--ink);
  }
</style>
</head>
<body>
<main class="stage">
  <section class="card card-front" aria-label="Card front">
    <span class="brand-dot" aria-hidden="true"></span>
    <span class="brand-name">Amber Finch</span>
  </section>

  <section class="card card-back" aria-label="Card back">
    <div class="back-brand">
      <span class="brand-dot" aria-hidden="true"></span>
      <span class="brand-name">Amber Finch</span>
    </div>
    <div class="contact-band" aria-hidden="true"></div>
    <ul class="contact-list">
      <li class="contact-item">
        <span class="contact-icon"><svg viewBox="0 0 24 24" fill="#fff"><path d="M6.6 10.8a15.1 15.1 0 0 0 6.6 6.6l2.2-2.2c.3-.3.7-.4 1-.2 1.1.4 2.3.6 3.6.6.6 0 1 .4 1 1V20c0 .6-.4 1-1 1C10.6 21 3 13.4 3 4c0-.6.4-1 1-1h3.5c.6 0 1 .4 1 1 0 1.3.2 2.5.6 3.6.1.3 0 .7-.2 1z"/></svg></span>
        <span class="contact-text">01492 718 263</span>
      </li>
      <li class="contact-item">
        <span class="contact-icon"><svg viewBox="0 0 24 24" fill="none" stroke="#fff" stroke-width="2"><rect x="3" y="5" width="18" height="14" rx="1"/><path d="M3 6l9 7 9-7"/></svg></span>
        <span class="contact-text">rowan@amberfinchevents.co.uk</span>
      </li>
      <li class="contact-item">
        <span class="contact-icon"><svg viewBox="0 0 24 24" fill="none" stroke="#fff" stroke-width="2"><rect x="3" y="5" width="18" height="14" rx="1"/><path d="M3 6l9 7 9-7"/></svg></span>
        <span class="contact-text">helena@amberfinchevents.co.uk</span>
      </li>
      <li class="contact-item">
        <span class="contact-icon"><svg viewBox="0 0 24 24" fill="none" stroke="#fff" stroke-width="2"><rect x="3" y="4" width="18" height="12" rx="1"/><path d="M9 20h6M12 16v4"/></svg></span>
        <span class="contact-text">amberfinchevents.co.uk</span>
      </li>
    </ul>
  </section>
</main>
</body>
</html>
```